Fontaneau Bayou Grillhouse (Owners Card)

Need a classy, but modern business card. I have included a promotional card for the steakhouse. I need one for myself (the owner) that is more professional.

Target Market(s)

General Public

Industry/Entity Type

Food service

Contact Information for Business Card

Name, business address, phone number, email, logo

Font styles to use
Serif
Sans Serif
Decorative
Script

Requirements
Must have
• My name (Darvin Okafor), business address (627 Harlow Avenue), phone number (520) 394-2751, email (Dokaforzp4@mailbrook.net. On the back of the card: Psalms 27 1 The LORD is my light and my salvation— whom shall I fear? The LORD is the stronghold of my life— of whom shall I be afraid? 2 When the wicked advance against me to devour me, it is my enemies and my foes who will stumble and fall. 3 Though an army besiege me, my heart will not fear; though war break out against me, even then I will be confident.
Nice to have
• Something that’s bold, but modern and professional.

```html
<!DOCTYPE html>
<html lang="en">
<head>
<meta charset="utf-8">
<title>Fontaneau Bayou Grillhouse — Owner Card</title>
<link rel="stylesheet" href="https://fonts.googleapis.com/css2?family=Open+Sans:wght@400;600;700&display=swap">
<style>
  :root {
    --backdrop: #e9e9eb;
    --card: #000000;
    --ink: #ffffff;
    --brand: #f28a1c;
    --warm-1: #ffd21a;
    --warm-2: #ff8a1a;
    --warm-3: #ff4d12;
    --rule: #ffffff;
  }
  html, body {
    margin: 0;
    padding: 0;
    width: 1200px;
    height: 1108px;
    overflow: hidden;
    background: var(--backdrop);
    font-family: "Open Sans", Arial, sans-serif;
  }
  .canvas {
    position: relative;
    width: 1200px;
    height: 1108px;
  }
  .card {
    position: absolute;
    background: var(--card);
    color: var(--ink);
  }
  .card--front { left: 230px; top: 70px; width: 776px; height: 445px; }
  .card--back  { left: 230px; top: 582px; width: 788px; height: 451px; }

  .brand {
    position: absolute;
    left: 0; right: 0;
    display: flex;
    align-items: center;
    justify-content: center;
    gap: 12px;
    font-weight: 700;
    font-size: 27px;
    letter-spacing: 0.5px;
    color: var(--brand);
  }
  .brand__dot {
    width: 18px; height: 18px;
    border-radius: 50%;
    background: var(--brand);
  }
  .card--front .brand { top: 150px; }
  .card--back .brand { top: 140px; }

  .owner-name {
    position: absolute;
    top: 216px; left: 0; right: 0;
    margin: 0;
    text-align: center;
    font-size: 35px;
    font-weight: 700;
    background: linear-gradient(90deg, var(--warm-1), var(--warm-2) 55%, var(--warm-3));
    -webkit-background-clip: text;
    background-clip: text;
    color: transparent;
  }
  .contact-divider {
    position: absolute;
    top: 277px; left: 212px;
    width: 356px;
    display: flex;
    align-items: center;
    gap: 4px;
  }
  .contact-divider__rule { flex: 1; height: 2px; background: var(--rule); }
  .contact-divider__icons { display: flex; gap: 3px; padding: 0 12px; }
  .contact-divider__icons svg { width: 29px; height: 29px; display: block; }

  .contact-list {
    position: absolute;
    top: 316px; left: 0; right: 0;
    margin: 0; padding: 0;
    list-style: none;
    text-align: center;
    font-size: 23px;
    line-height: 34.5px;
  }

  .scripture {
    position: absolute;
    top: 204px; left: 0; right: 0;
  }
  .scripture__title {
    margin: 0 0 3px;
    text-align: center;
    font-size: 21px;
    font-weight: 700;
  }
  .scripture__verses {
    margin: 0; padding: 0;
    list-style: none;
  }
  .scripture__verse {
    position: relative;
    padding: 0 55px 0 101px;
    font-size: 20px;
    line-height: 33px;
    text-align: justify;
  }
  .scripture__num {
    position: absolute;
    left: 54px; top: 0;
  }
</style>
</head>
<body>
<div class="canvas">

  <section class="card card--front">
    <div class="brand"><span class="brand__dot"></span>Fontaneau Bayou Grillhouse</div>
    <h1 class="owner-name">Darvin Okafor</h1>
    <div class="contact-divider">
      <span class="contact-divider__rule"></span>
      <span class="contact-divider__icons">
        <svg viewBox="0 0 30 30" aria-hidden="true">
          <circle cx="15" cy="15" r="14" fill="var(--warm-2)"/>
          <path d="M10 8.5c1-.8 2-.6 2.6.3l1.4 2.2c.4.7.2 1.4-.4 1.9l-.9.7c.8 1.8 2.1 3.1 3.9 3.9l.7-.9c.5-.6 1.2-.8 1.9-.4l2.2 1.4c.9.6 1.1 1.6.3 2.6-1 1.2-2.4 1.7-4 1.1-4.3-1.6-7.3-4.6-8.9-8.9-.6-1.6-.1-3 1.2-3.9z" fill="#1a0a00"/>
        </svg>
        <svg viewBox="0 0 30 30" aria-hidden="true">
          <circle cx="15" cy="15" r="14" fill="var(--warm-3)"/>
          <rect x="7.5" y="9.5" width="15" height="11" rx="1.2" fill="none" stroke="#1a0a00" stroke-width="2"/>
          <path d="M8 10.5l7 6 7-6M8 19.5l5-4.5M22 19.5l-5-4.5" fill="none" stroke="#1a0a00" stroke-width="1.8"/>
        </svg>
        <svg viewBox="0 0 30 30" aria-hidden="true">
          <circle cx="15" cy="15" r="14" fill="var(--warm-2)"/>
          <path d="M15 6.5c-3.3 0-5.8 2.5-5.8 5.7 0 4.2 5.8 11 5.8 11s5.8-6.8 5.8-11c0-3.2-2.5-5.7-5.8-5.7z" fill="#1a0a00"/>
          <circle cx="15" cy="12.2" r="2.2" fill="var(--warm-1)"/>
        </svg>
      </span>
      <span class="contact-divider__rule"></span>
    </div>
    <ul class="contact-list">
      <li class="contact-list__phone">(520) 394-2751</li>
      <li class="contact-list__email">Dokaforzp4@mailbrook.net</li>
      <li class="contact-list__address">627 Harlow Avenue</li>
    </ul>
  </section>

  <section class="card card--back">
    <div class="brand"><span class="brand__dot"></span>Fontaneau Bayou Grillhouse</div>
    <div class="scripture">
      <h2 class="scripture__title">Psalms 27</h2>
      <ol class="scripture__verses">
        <li class="scripture__verse"><span class="scripture__num">1</span>The LORD is my light and my salvation— whom shall I fear? The LORD is the stronghold of my life— of whom shall I be afraid?</li>
        <li class="scripture__verse"><span class="scripture__num">2</span>When the wicked advance against me to devour me, it is my enemies and my foes who will stumble and fall.</li>
        <li class="scripture__verse"><span class="scripture__num">3</span>Though an army besiege me, my heart will not fear; though war break out against me, even then I will be confident.</li>
      </ol>
    </div>
  </section>

</div>
</body>
</html>
```